PowerPoint template for a tech startup

We need a PowerPoint template with a title slide, text slide, section slide, and thank you slide.
Our application helps engineering teams to be more productive. We would love a design that is slick, sophisticated, and consistent with our brand. (see more at www.quenvomi.io or attached files)
By the way (not a requirement), Quenvo means lighthouse in Greek.
Also, here is the font we used (not required) - https://fonts.trelvanic.com/fonts/league-gothic

Other font styles liked:
• https://fonts.trelvanic.com/fonts/league-gothic

```html
<!DOCTYPE html>
<html lang="en">
<head>
<meta charset="utf-8">
<title>Quenvo Presentation Template</title>
<link rel="stylesheet" href="https://fonts.googleapis.com/css2?family=League+Gothic&family=Montserrat:wght@400;600;700&display=swap">
<style>
:root{
  --blue:#1d5075;
  --blue-dark:#173f5e;
  --orange:#e8590c;
  --orange-soft:#f07a3a;
  --purple:#8b6cf0;
  --ink:#1d5075;
  --grey:#8a8f96;
  --line:#d6d9de;
  --white:#ffffff;
  --stage-top:#e9ebee;
  --stage-bottom:#d6d7da;
}
*{box-sizing:border-box;margin:0;padding:0}
html,body{width:680px;height:1200px;overflow:hidden}
body{
  position:relative;
  font-family:"Montserrat",Arial,sans-serif;
  background:linear-gradient(180deg,var(--stage-top) 0,var(--stage-top) 400px,var(--stage-bottom) 410px,var(--stage-bottom) 100%);
}
.display{font-family:"League Gothic","Oswald",Impact,sans-serif;font-weight:400;letter-spacing:.2px}
.brand-mark{position:absolute;font-family:"League Gothic",Impact,sans-serif;color:var(--blue);line-height:1}
.brand-mark--hero{top:30px;right:38px;font-size:46px;letter-spacing:1px}

.hero{position:absolute;left:130px;top:106px;width:216px;height:121px;transform:scale(1.944);transform-origin:0 0;box-shadow:0 2px 6px rgba(0,0,0,.18)}

.gallery{position:absolute;left:9px;top:424px;display:grid;grid-template-columns:repeat(3,216px);grid-auto-rows:121px;gap:7px 7px}

.slide{position:relative;width:216px;height:121px;overflow:hidden;background:var(--white);color:var(--ink)}
.slide--blue{background:var(--blue);color:var(--white)}
.slide--orange{background:var(--orange);color:var(--white)}
.slide--blend{background:linear-gradient(110deg,var(--blue) 0%,var(--blue) 35%,var(--orange) 100%);color:var(--white)}
.slide--blend-rev{background:linear-gradient(110deg,var(--blue) 0%,var(--blue) 30%,var(--orange) 100%);color:var(--white)}

.gear-art{position:absolute;right:0;top:0;width:95px;height:75px;background:radial-gradient(ellipse at 75% 30%,rgba(255,255,255,.16),rgba(255,255,255,0) 70%)}
.slide--white .gear-art{background:radial-gradient(ellipse at 75% 30%,rgba(29,80,117,.10),rgba(29,80,117,0) 70%)}
.gear-art--low{position:absolute;left:0;bottom:0;width:70px;height:40px;background:radial-gradient(ellipse at 20% 80%,rgba(232,89,12,.10),rgba(232,89,12,0) 70%)}

.logo{position:absolute;font-family:"League Gothic",Impact,sans-serif;line-height:1;color:inherit}
.slide--white .logo,.slide--content .logo{color:var(--blue)}
.logo--title{left:20px;top:20px;font-size:19px}
.logo--corner{right:8px;top:7px;font-size:10px;color:var(--blue)}

.title-main{position:absolute;left:20px;top:53px;font-size:14.5px;line-height:1.12;text-transform:uppercase}
.slide--white .title-main{color:var(--blue)}
.title-sub{position:absolute;left:123px;top:58px;font-size:7px;line-height:1.05}
.slide--white .title-sub{color:var(--orange)}
.date-pill{position:absolute;left:20px;top:93px;width:47px;height:7px;background:var(--orange);color:var(--white);font-size:2.8px;line-height:7px;text-align:center;border-radius:1px}
.date-pill--outline{background:none;border:.5px solid var(--white);top:auto;bottom:8px}
.copyright{position:absolute;bottom:4px;left:0;right:0;text-align:center;font-size:2.2px;opacity:.85}
.slide--white .copyright{color:var(--grey)}
.copyright--left{left:4px;text-align:left;color:var(--grey)}

.band{position:absolute;left:0;right:0;top:29px;height:82px;background:var(--blue);color:var(--white)}
.band--blend{background:linear-gradient(100deg,var(--blue) 10%,#9a4f50 55%,var(--orange) 100%)}
.band .gear-art{height:60px}
.band-title{position:absolute;left:20px;top:12px;font-size:11.5px;line-height:1.15;text-transform:uppercase}
.band-body{position:absolute;left:20px;top:45px;width:120px;font-size:2.9px;line-height:1.2}
.logo--above{left:20px;top:7px;font-size:18px;color:var(--blue)}
.copyright--below{bottom:2px;color:var(--grey)}

.toc-head{position:absolute;left:0;right:0;top:0;height:60px;background:var(--blue)}
.toc-head .logo{left:0;right:0;top:15px;text-align:center;font-size:26px;color:var(--white)}
.toc-label{position:absolute;left:16px;top:80px;font-size:7px;line-height:1.1;text-align:center;color:var(--blue)}
.toc-label b{font-weight:700}
.toc-grid{position:absolute;left:62px;top:67px;display:grid;grid-template-columns:repeat(4,39px);row-gap:6px}
.toc-item{font-size:3px;line-height:1.1;color:var(--orange)}
.toc-item b{font-weight:700}
.toc-item small{display:block;font-size:2px;color:var(--grey);margin-top:1px}
.toc-rule{position:absolute;left:0;right:0;bottom:0;height:1.5px;background:var(--orange)}

.slide--content::after{content:"";position:absolute;left:0;right:0;bottom:0;height:1.5px;background:var(--orange)}
.slide-title{position:absolute;left:8px;top:8px;font-size:9.5px;color:var(--blue);padding-left:7px;text-transform:uppercase}
.slide-title::before{content:"";position:absolute;left:0;top:1px;width:3px;height:10px;background:var(--orange)}
.page-no{position:absolute;right:5px;bottom:4px;font-size:2.2px;color:var(--grey)}
.lorem{font-size:2.4px;line-height:1.25;color:var(--grey)}

.photo{position:absolute;left:13px;top:0;width:101px;height:105px;background:linear-gradient(135deg,#e7e9ec,#b9bec5)}
.about-title{position:absolute;left:123px;top:27px;font-size:10px;color:var(--blue)}
.about-sub{position:absolute;left:123px;top:40px;font-size:3.4px;color:var(--orange)}
.about-list{position:absolute;left:128px;top:52px;width:78px;list-style:none}
.about-list li{position:relative;margin-bottom:3px}
.about-list li::before{content:"";position:absolute;left:-4px;top:1px;width:1.2px;height:1.2px;background:var(--orange)}

.icon{display:inline-block;border-radius:50%;position:relative}
.icon::after{content:"";position:absolute;left:32%;top:32%;width:36%;height:36%;border-radius:50%;border:1px solid var(--white)}
.icon--blue{background:var(--blue)}
.icon--orange{background:var(--orange)}
.icon--purple{background:var(--purple)}

.steps{position:absolute;left:16px;right:16px;top:28px;display:flex;justify-content:space-between}
.steps::before{content:"";position:absolute;left:-10px;right:-8px;top:8px;height:1px;background:#e4e6ea}
.step{position:relative;width:54px;text-align:center}
.step .icon{width:17px;height:17px}
.step h3{font-size:5px;line-height:1.1;margin:3px 0 5px;font-weight:700}
.step h3 span{font-weight:400;display:block}
.step--blue h3{color:var(--blue)}.step--orange h3{color:var(--orange)}.step--purple h3{color:var(--purple)}

.section-logo{position:absolute;left:20px;top:42px;font-size:19px;color:var(--white)}
.section-title{position:absolute;left:20px;top:70px;font-size:11.5px;color:var(--white);text-transform:uppercase}
.section-text{position:absolute;left:20px;top:85px;width:105px;font-size:3.2px;line-height:1.2;color:var(--white)}
.photo-wash{position:absolute;inset:0}
.photo-wash--blue{background:linear-gradient(135deg,rgba(255,255,255,.05),rgba(0,0,0,.08))}
.photo-wash--orange{background:linear-gradient(135deg,rgba(255,255,255,.06),rgba(0,0,0,.08))}

.rows{position:absolute;left:8px;right:8px;top:25px;display:flex;flex-direction:column;gap:4px}
.row{display:flex;align-items:center;gap:4px}
.row .icon{width:11px;height:11px;flex:none;margin-right:-6px;z-index:1;box-shadow:0 0 0 1.5px var(--white)}
.row-tag{width:50px;height:18px;background:var(--blue);color:var(--white);font-size:4px;line-height:1.05;padding:5px 0 0 10px;border-radius:0 1px 1px 0;flex:none}
.row-tag b{font-weight:700;display:block}
.row-box{flex:1;height:22px;border:.5px solid var(--line);padding:3px 3px 0 6px}

.pairs{position:absolute;left:26px;right:20px;top:23px;display:grid;grid-template-columns:1fr 1fr;row-gap:6px;column-gap:6px}
.pair{display:flex;align-items:center;gap:4px;height:18px}
.pair--left{flex-direction:row-reverse;text-align:right}
.pair .icon{width:12px;height:12px;flex:none}
.pair h3{font-size:4.8px;font-weight:400;color:var(--blue)}
.pair h3 b{color:var(--orange);font-weight:700}
.pair--plain h3 b{color:var(--blue)}
.pair .lorem{font-size:2.2px}

.chart-text{position:absolute;left:16px;top:33px;width:76px}
.chart-text h3{font-size:5px;font-weight:400;margin-bottom:2px}
.chart-text h3 b{font-weight:700}
.chart-text .lorem{margin-bottom:6px}
.h-blue{color:var(--blue)}.h-orange{color:var(--orange)}.h-purple{color:var(--purple)}
.bar-chart{position:absolute;left:110px;top:32px;width:96px;height:75px}

.donuts{position:absolute;left:24px;right:24px;top:30px;display:flex;justify-content:space-between}
.donut{width:46px;text-align:center}
.donut svg{width:46px;height:46px}
.donut h3{font-size:5px;font-weight:400;margin:3px 0 2px}
.donut .lorem{font-size:2.1px}

.contact{position:absolute;left:32px;top:33px;color:var(--white)}
.contact .logo{position:static;font-size:19px;color:var(--white)}
.contact h3{font-family:"League Gothic",Impact,sans-serif;font-weight:400;font-size:6px;margin:5px 0 4px}
.contact ul{list-style:none;font-size:3px;line-height:1}
.contact li{display:flex;align-items:center;gap:3px;margin-bottom:2.6px}
.contact svg{width:4px;height:4px}
.contact--left{left:20px}
.contact-bg{position:absolute;left:0;right:0;top:0;bottom:10px}
.contact-bg--blue{background:var(--blue)}
.contact-bg--blend{background:linear-gradient(110deg,var(--blue) 0%,var(--blue) 30%,var(--orange) 100%)}
</style>
</head>
<body>

<div class="brand-mark brand-mark--hero">QUENVO</div>

<section class="hero slide slide--white">
  <div class="gear-art" role="img" aria-label="Faint gear and blueprint pattern"></div>
  <div class="gear-art--low" role="img" aria-label="Faint gear pattern"></div>
  <div class="logo logo--title">QUENVO</div>
  <h1 class="title-main display">Presentation Title<br>Goes Here!</h1>
  <p class="title-sub">Subtitle of<br>Presentation<br>Goes Here!</p>
  <div class="date-pill">Monday, March 14, 2022</div>
  <p class="copyright">Copyright © 2022, Quenvo AI, Inc. All Rights Reserved.</p>
</section>

<main class="gallery">

  <section class="slide slide--blue">
    <div class="gear-art" role="img" aria-label="Faint gear and blueprint pattern"></div>
    <div class="logo logo--title">QUENVO</div>
    <h2 class="title-main display">Presentation Title<br>Goes Here!</h2>
    <p class="title-sub">Subtitle of<br>Presentation<br>Goes Here!</p>
    <div class="date-pill">Monday, March 14, 2022</div>
    <p class="copyright">Copyright © 2022, Quenvo AI, Inc. All Rights Reserved.</p>
  </section>

  <section class="slide slide--white">
    <div class="gear-art" role="img" aria-label="Faint gear and blueprint pattern"></div>
    <div class="gear-art--low" role="img" aria-label="Faint gear pattern"></div>
    <div class="logo logo--title">QUENVO</div>
    <h2 class="title-main display">Presentation Title<br>Goes Here!</h2>
    <p class="title-sub">Subtitle of<br>Presentation<br>Goes Here!</p>
    <div class="date-pill">Monday, March 14, 2022</div>
    <p class="copyright">Copyright © 2022, Quenvo AI, Inc. All Rights Reserved.</p>
  </section>

  <section class="slide slide--blend">
    <div class="gear-art" role="img" aria-label="Faint gear and blueprint pattern"></div>
    <div class="logo logo--title">QUENVO</div>
    <h2 class="title-main display">Presentation Title<br>Goes Here!</h2>
    <p class="title-sub">Subtitle of<br>Presentation<br>Goes Here!</p>
    <div class="date-pill">Monday, March 14, 2022</div>
    <p class="copyright">Copyright © 2022, Quenvo AI, Inc. All Rights Reserved.</p>
  </section>

  <section class="slide slide--white">
    <div class="logo logo--above">QUENVO</div>
    <div class="band">
      <div class="gear-art" role="img" aria-label="Faint gear pattern"></div>
      <h2 class="band-title display">The Unified<br>Engineering Insights Workspace</h2>
      <p class="band-body">Quenvo AI links every signal across your engineering tools – issues, code reviews, builds, deploys and more – delivering clear visibility and practical insight into how your teams ship work.</p>
      <div class="date-pill date-pill--outline">Monday, March 14, 2022</div>
    </div>
    <p class="copyright copyright--below">Copyright © 2022, Quenvo AI, Inc. All Rights Reserved.</p>
  </section>

  <section class="slide slide--white">
    <div class="logo logo--above">QUENVO</div>
    <div class="band band--blend">
      <div class="gear-art" role="img" aria-label="Faint gear pattern"></div>
      <h2 class="band-title display">The Unified<br>Engineering Insights Workspace</h2>
      <p class="band-body">Quenvo AI links every signal across your engineering tools – issues, code reviews, builds, deploys and more – delivering clear visibility and practical insight into how your teams ship work.</p>
      <div class="date-pill date-pill--outline">Monday, March 14, 2022</div>
    </div>
    <p class="copyright copyright--below">Copyright © 2022, Quenvo AI, Inc. All Rights Reserved.</p>
  </section>

  <section class="slide slide--white">
    <div class="toc-head" role="img" aria-label="Blue-tinted photo of a desk with blueprints">
      <div class="logo">QUENVO</div>
    </div>
    <p class="toc-label">Table of<br><b>Contents</b></p>
    <div class="toc-grid">
      <p class="toc-item"><b>Your Title</b><br>Goes Here<small>Consectetur<br>Adipiscing Vivamus</small></p>
      <p class="toc-item"><b>Your Title</b><br>Goes Here<small>Consectetur<br>Adipiscing Vivamus</small></p>
      <p class="toc-item"><b>Your Title</b><br>Goes Here<small>Consectetur<br>Adipiscing Vivamus</small></p>
      <p class="toc-item"><b>Your Title</b><br>Goes Here<small>Consectetur<br>Adipiscing Vivamus</small></p>
      <p class="toc-item"><b>Your Title</b><br>Goes Here<small>Consectetur<br>Adipiscing Vivamus</small></p>
      <p class="toc-item"><b>Your Title</b><br>Goes Here<small>Consectetur<br>Adipiscing Vivamus</small></p>
      <p class="toc-item"><b>Your Title</b><br>Goes Here<small>Consectetur<br>Adipiscing Vivamus</small></p>
      <p class="toc-item"><b>Your Title</b><br>Goes Here<small>Consectetur<br>Adipiscing Vivamus</small></p>
    </div>
    <p class="copyright copyright--left">Copyright © 2022, Quenvo AI, Inc. All Rights Reserved.</p>
    <div class="toc-rule"></div>
  </section>

  <section class="slide slide--content">
    <div class="photo" role="img" aria-label="Photo of engineering drawings with drafting tools"></div>
    <div class="logo logo--corner">QUENVO</div>
    <h2 class="about-title display">ABOUT US</h2>
    <p class="about-sub">Subtitle Goes Here</p>
    <ul class="about-list lorem">
      <li>Lorem ipsum dolor sit amet, consectetur adipiscing elit. Vivamus eu dui ex. Curabitur dapibus dignissim dui, in molestie metus feugiat sed. Praesent aliquet lorem ex.</li>
      <li>Duis eget tellus porta, consequat lacus vitae, venenatis dolor. Nulla facilisi. In et sollicitudin lacus. Donec risus orci, gravida sit amet risus vehicula, aliquet pretium sapien.</li>
    </ul>
    <p class="copyright copyright--left">Copyright © 2022, Quenvo AI, Inc. All Rights Reserved.</p>
    <span class="page-no">7</span>
  </section>

  <section class="slide slide--content">
    <h2 class="slide-title display">Slide Title Goes Here!</h2>
    <div class="logo logo--corner">QUENVO</div>
    <div class="steps">
      <div class="step step--blue"><span class="icon icon--blue"></span><h3>Heading<span>Goes Here</span></h3><p class="lorem">Lorem ipsum dolor sit amet, consectetur adipiscing elit. Vivamus eu dui ex. Curabitur dapibus dignissim dui, in molestie metus feugiat sed.</p></div>
      <div class="step step--orange"><span class="icon icon--orange"></span><h3>Heading<span>Goes Here</span></h3><p class="lorem">Lorem ipsum dolor sit amet, consectetur adipiscing elit. Vivamus eu dui ex. Curabitur dapibus dignissim dui, in molestie metus feugiat sed.</p></div>
      <div class="step step--purple"><span class="icon icon--purple"></span><h3>Heading<span>Goes Here</span></h3><p class="lorem">Lorem ipsum dolor sit amet, consectetur adipiscing elit. Vivamus eu dui ex. Curabitur dapibus dignissim dui, in molestie metus feugiat sed.</p></div>
    </div>
    <p class="copyright copyright--left">Copyright © 2022, Quenvo AI, Inc. All Rights Reserved.</p>
    <span class="page-no">8</span>
  </section>

  <section class="slide slide--blue">
    <div class="photo-wash photo-wash--blue" role="img" aria-label="Blue-tinted photo of blueprints and drafting tools"></div>
    <div class="gear-art" role="img" aria-label="Faint gear pattern"></div>
    <div class="logo section-logo">QUENVO</div>
    <h2 class="section-title display">Section Break</h2>
    <p class="section-text">Lorem ipsum dolor sit amet, consectetur adipiscing elit. Vivamus eu dui ex. Curabitur dapibus dignissim dui, in molestie metus feugiat sed.</p>
  </section>

  <section class="slide slide--content">
    <h2 class="slide-title display">Slide Title Goes Here!</h2>
    <div class="logo logo--corner">QUENVO</div>
    <div class="rows">
      <div class="row"><span class="icon icon--orange"></span><div class="row-tag"><b>Heading</b>Goes Here</div><p class="row-box lorem">Lorem ipsum dolor sit amet, consectetur adipiscing elit. Vivamus eu dui ex. Curabitur dapibus dignissim dui, in molestie metus feugiat sed. Praesent aliquet lorem ex, eu dapibus odio varius at.</p></div>
      <div class="row"><span class="icon icon--orange"></span><div class="row-tag"><b>Heading</b>Goes Here</div><p class="row-box lorem">Lorem ipsum dolor sit amet, consectetur adipiscing elit. Vivamus eu dui ex. Curabitur dapibus dignissim dui, in molestie metus feugiat sed. Praesent aliquet lorem ex, eu dapibus odio varius at.</p></div>
      <div class="row"><span class="icon icon--orange"></span><div class="row-tag"><b>Heading</b>Goes Here</div><p class="row-box lorem">Lorem ipsum dolor sit amet, consectetur adipiscing elit. Vivamus eu dui ex. Curabitur dapibus dignissim dui, in molestie metus feugiat sed. Praesent aliquet lorem ex, eu dapibus odio varius at.</p></div>
    </div>
    <p class="copyright copyright--left">Copyright © 2022, Quenvo AI, Inc. All Rights Reserved.</p>
    <span class="page-no">10</span>
  </section>

  <section class="slide slide--content">
    <h2 class="slide-title display">Slide Title Goes Here!</h2>
    <div class="logo logo--corner">QUENVO</div>
    <div class="pairs">
      <div class="pair pair--left"><span class="icon icon--blue"></span><div><h3><b>Heading</b> Goes Here</h3><p class="lorem">Lorem ipsum dolor sit amet, consectetur adipiscing elit.</p></div></div>
      <div class="pair"><span class="icon icon--orange"></span><div><h3><b>Heading</b> Goes Here</h3><p class="lorem">Lorem ipsum dolor sit amet, consectetur adipiscing elit.</p></div></div>
      <div class="pair pair--left"><span class="icon icon--orange"></span><div><h3><b>Heading</b> Goes Here</h3><p class="lorem">Lorem ipsum dolor sit amet, consectetur adipiscing elit.</p></div></div>
      <div class="pair pair--plain"><span class="icon icon--blue"></span><div><h3><b>Heading</b> Goes Here</h3><p class="lorem">Lorem ipsum dolor sit amet, consectetur adipiscing elit.</p></div></div>
      <div class="pair pair--left pair--plain"><span class="icon icon--blue"></span><div><h3><b>Heading</b> Goes Here</h3><p class="lorem">Lorem ipsum dolor sit amet, consectetur adipiscing elit.</p></div></div>
      <div class="pair"><span class="icon icon--orange"></span><div><h3><b>Heading</b> Goes Here</h3><p class="lorem">Lorem ipsum dolor sit amet, consectetur adipiscing elit.</p></div></div>
    </div>
    <p class="copyright copyright--left">Copyright © 2022, Quenvo AI, Inc. All Rights Reserved.</p>
    <span class="page-no">11</span>
  </section>

  <section class="slide slide--orange">
    <div class="photo-wash photo-wash--orange" role="img" aria-label="Orange-tinted photo of hands working on a laptop"></div>
    <div class="gear-art" role="img" aria-label="Faint gear pattern"></div>
    <div class="logo section-logo">QUENVO</div>
    <h2 class="section-title display">Section Break</h2>
    <p class="section-text">Lorem ipsum dolor sit amet, consectetur adipiscing elit. Vivamus eu dui ex. Curabitur dapibus dignissim dui, in molestie metus feugiat sed.</p>
  </section>

  <section class="slide slide--content">
    <h2 class="slide-title display">Slide Title Goes Here</h2>
    <div class="logo logo--corner">QUENVO</div>
    <div class="chart-text">
      <h3 class="h-blue"><b>Heading</b> Goes Here</h3><p class="lorem">Lorem ipsum dolor sit amet, consectetur adipiscing elit. Vivamus eu dui ex.</p>
      <h3 class="h-orange"><b>Heading</b> Goes Here</h3><p class="lorem">Lorem ipsum dolor sit amet, consectetur adipiscing elit. Vivamus eu dui ex.</p>
      <h3 class="h-purple"><b>Heading</b> Goes Here</h3><p class="lorem">Lorem ipsum dolor sit amet, consectetur adipiscing elit. Vivamus eu dui ex.</p>
    </div>
    <svg class="bar-chart" viewBox="0 0 96 75" role="img" aria-label="Grouped bar chart for categories A, B and C">
      <g stroke="#e4e6ea" stroke-width=".4"><line x1="0" y1="2" x2="0" y2="65"/><line x1="32" y1="2" x2="32" y2="65"/><line x1="64" y1="2" x2="64" y2="65"/><line x1="96" y1="2" x2="96" y2="65"/></g>
      <g><rect x="8" y="17" width="3" height="48" fill="#1d5075"/><rect x="13" y="38" width="3" height="27" fill="#e8590c"/><rect x="18" y="43" width="3" height="22" fill="#8b6cf0"/></g>
      <g><rect x="40" y="37" width="3" height="28" fill="#1d5075"/><rect x="45" y="15" width="3" height="50" fill="#e8590c"/><rect x="50" y="43" width="3" height="22" fill="#8b6cf0"/></g>
      <g><rect x="72" y="25" width="3" height="40" fill="#1d5075"/><rect x="77" y="45" width="3" height="20" fill="#e8590c"/><rect x="82" y="29" width="3" height="36" fill="#8b6cf0"/></g>
      <g font-size="2.6" fill="#8a8f96" font-family="Montserrat,sans-serif" text-anchor="middle"><text x="14" y="70">A</text><text x="46" y="70">B</text><text x="78" y="70">C</text></g>
    </svg>
    <p class="copyright copyright--left">Copyright © 2022, Quenvo AI, Inc. All Rights Reserved.</p>
    <span class="page-no">13</span>
  </section>

  <section class="slide slide--content">
    <h2 class="slide-title display">Slide Title Goes Here</h2>
    <div class="logo logo--corner">QUENVO</div>
    <div class="donuts">
      <div class="donut"><svg viewBox="0 0 46 46" role="img" aria-label="64 percent"><circle cx="23" cy="23" r="20" fill="none" stroke="#eceef1" stroke-width="2.5"/><circle cx="23" cy="23" r="20" fill="none" stroke="#1d5075" stroke-width="2.5" stroke-dasharray="80.4 125.7" transform="rotate(-90 23 23)"/><text x="23" y="26" text-anchor="middle" font-size="9" fill="#1d5075" font-family="Montserrat,sans-serif">64<tspan font-size="4">%</tspan></text></svg><h3 class="h-blue">Heading</h3><p class="lorem">Lorem ipsum dolor sit amet, consectetur adipiscing elit.</p></div>
      <div class="donut"><svg viewBox="0 0 46 46" role="img" aria-label="82 percent"><circle cx="23" cy="23" r="20" fill="none" stroke="#eceef1" stroke-width="2.5"/><circle cx="23" cy="23" r="20" fill="none" stroke="#e8590c" stroke-width="2.5" stroke-dasharray="103 125.7" transform="rotate(-90 23 23)"/><text x="23" y="26" text-anchor="middle" font-size="9" fill="#e8590c" font-family="Montserrat,sans-serif">82<tspan font-size="4">%</tspan></text></svg><h3 class="h-orange">Heading</h3><p class="lorem">Lorem ipsum dolor sit amet, consectetur adipiscing elit.</p></div>
      <div class="donut"><svg viewBox="0 0 46 46" role="img" aria-label="94 percent"><circle cx="23" cy="23" r="20" fill="none" stroke="#eceef1" stroke-width="2.5"/><circle cx="23" cy="23" r="20" fill="none" stroke="#8b6cf0" stroke-width="2.5" stroke-dasharray="118.2 125.7" transform="rotate(-90 23 23)"/><text x="23" y="26" text-anchor="middle" font-size="9" fill="#8b6cf0" font-family="Montserrat,sans-serif">94<tspan font-size="4">%</tspan></text></svg><h3 class="h-purple">Heading</h3><p class="lorem">Lorem ipsum dolor sit amet, consectetur adipiscing elit.</p></div>
    </div>
    <p class="copyright copyright--left">Copyright © 2022, Quenvo AI, Inc. All Rights Reserved.</p>
    <span class="page-no">14</span>
  </section>

  <section class="slide slide--blue">
    <div class="photo-wash photo-wash--blue" role="img" aria-label="Blue-tinted photo of a business meeting"></div>
    <div class="gear-art" role="img" aria-label="Faint gear pattern"></div>
    <div class="contact">
      <div class="logo">QUENVO</div>
      <h3>CONTACT US</h3>
      <ul>
        <li><svg viewBox="0 0 10 10"><path d="M2 1h2l1 2.5-1.3 1a5 5 0 0 0 1.8 1.8l1-1.3L9 6v2c0 .6-.4 1-1 1A8 8 0 0 1 1 2c0-.6.4-1 1-1z" fill="#fff"/></svg>Insert Phone Number</li>
        <li><svg viewBox="0 0 10 10"><circle cx="5" cy="5" r="4" fill="none" stroke="#fff" stroke-width="1.2"/><circle cx="5" cy="5" r="1.6" fill="#fff"/></svg>Insert E-Mail Address</li>
        <li><svg viewBox="0 0 10 10"><circle cx="5" cy="5" r="4" fill="none" stroke="#fff" stroke-width="1"/><path d="M1 5h8M5 1c2 2 2 6 0 8M5 1c-2 2-2 6 0 8" fill="none" stroke="#fff" stroke-width=".8"/></svg>Insert URL Address</li>
      </ul>
    </div>
    <p class="copyright" style="left:auto;right:12px;text-align:right">Copyright © 2022, Quenvo AI, Inc. All Rights Reserved.</p>
  </section>

  <section class="slide slide--blend-rev">
    <div class="photo-wash" role="img" aria-label="Tinted photo of a business meeting"></div>
    <div class="gear-art" role="img" aria-label="Faint gear pattern"></div>
    <div class="contact">
      <div class="logo">QUENVO</div>
      <h3>CONTACT US</h3>
      <ul>
        <li><svg viewBox="0 0 10 10"><path d="M2 1h2l1 2.5-1.3 1a5 5 0 0 0 1.8 1.8l1-1.3L9 6v2c0 .6-.4 1-1 1A8 8 0 0 1 1 2c0-.6.4-1 1-1z" fill="#fff"/></svg>Insert Phone Number</li>
        <li><svg viewBox="0 0 10 10"><circle cx="5" cy="5" r="4" fill="none" stroke="#fff" stroke-width="1.2"/><circle cx="5" cy="5" r="1.6" fill="#fff"/></svg>Insert E-Mail Address</li>
        <li><svg viewBox="0 0 10 10"><circle cx="5" cy="5" r="4" fill="none" stroke="#fff" stroke-width="1"/><path d="M1 5h8M5 1c2 2 2 6 0 8M5 1c-2 2-2 6 0 8" fill="none" stroke="#fff" stroke-width=".8"/></svg>Insert URL Address</li>
      </ul>
    </div>
    <p class="copyright">Copyright © 2022, Quenvo AI, Inc. All Rights Reserved.</p>
  </section>

  <section class="slide slide--white">
    <div class="contact-bg contact-bg--blue" role="img" aria-label="Blue-tinted photo of a business meeting"></div>
    <div class="gear-art" role="img" aria-label="Faint gear pattern" style="background:radial-gradient(ellipse at 75% 30%,rgba(255,255,255,.16),rgba(255,255,255,0) 70%)"></div>
    <div class="contact contact--left">
      <div class="logo">QUENVO</div>
      <h3>CONTACT US</h3>
      <ul>
        <li><svg viewBox="0 0 10 10"><path d="M2 1h2l1 2.5-1.3 1a5 5 0 0 0 1.8 1.8l1-1.3L9 6v2c0 .6-.4 1-1 1A8 8 0 0 1 1 2c0-.6.4-1 1-1z" fill="#fff"/></svg>Insert Phone Number</li>
        <li><svg viewBox="0 0 10 10"><circle cx="5" cy="5" r="4" fill="none" stroke="#fff" stroke-width="1.2"/><circle cx="5" cy="5" r="1.6" fill="#fff"/></svg>Insert E-Mail Address</li>
        <li><svg viewBox="0 0 10 10"><circle cx="5" cy="5" r="4" fill="none" stroke="#fff" stroke-width="1"/><path d="M1 5h8M5 1c2 2 2 6 0 8M5 1c-2 2-2 6 0 8" fill="none" stroke="#fff" stroke-width=".8"/></svg>Insert URL Address</li>
      </ul>
    </div>
    <p class="copyright copyright--below">Copyright © 2022, Quenvo AI, Inc. All Rights Reserved.</p>
  </section>

  <section class="slide slide--white">
    <div class="contact-bg contact-bg--blend" role="img" aria-label="Tinted photo of a business meeting"></div>
    <div class="gear-art" role="img" aria-label="Faint gear pattern" style="background:radial-gradient(ellipse at 75% 30%,rgba(255,255,255,.16),rgba(255,255,255,0) 70%)"></div>
    <div class="contact contact--left">
      <div class="logo">QUENVO</div>
      <h3>CONTACT US</h3>
      <ul>
        <li><svg viewBox="0 0 10 10"><path d="M2 1h2l1 2.5-1.3 1a5 5 0 0 0 1.8 1.8l1-1.3L9 6v2c0 .6-.4 1-1 1A8 8 0 0 1 1 2c0-.6.4-1 1-1z" fill="#fff"/></svg>Insert Phone Number</li>
        <li><svg viewBox="0 0 10 10"><circle cx="5" cy="5" r="4" fill="none" stroke="#fff" stroke-width="1.2"/><circle cx="5" cy="5" r="1.6" fill="#fff"/></svg>Insert E-Mail Address</li>
        <li><svg viewBox="0 0 10 10"><circle cx="5" cy="5" r="4" fill="none" stroke="#fff" stroke-width="1"/><path d="M1 5h8M5 1c2 2 2 6 0 8M5 1c-2 2-2 6 0 8" fill="none" stroke="#fff" stroke-width=".8"/></svg>Insert URL Address</li>
      </ul>
    </div>
    <p class="copyright copyright--below">Copyright © 2022, Quenvo AI, Inc. All Rights Reserved.</p>
  </section>

</main>
</body>
</html>
```